Mouse and Rodent Infestation Spray

Need to Design label for 16oz bottle. The image sent has our initial design on it. Need other options.

Industry/Entity Type

Pest Control

Colors

Designer to choose colors to be used in the design.

```html
<!DOCTYPE html>
<html lang="en">
<head>
<meta charset="utf-8">
<title>Mouse &amp; Rat Infestation Label</title>
<link rel="stylesheet" href="https://fonts.googleapis.com/css2?family=Anton&family=Oswald:wght@500;600;700&display=swap">
<style>
  :root {
    --red-deep: #6e0306;
    --red: #b00f16;
    --red-bright: #c8141c;
    --green: #3fae38;
    --green-dark: #2c8a29;
    --green-light: #6cc24a;
    --seal-dark: #23433f;
    --ink: #1f1f1f;
    --white: #ffffff;
    --page: #ffffff;
    --mouse-brown: #7a5234;
  }
  html, body {
    margin: 0;
    padding: 0;
    width: 1200px;
    height: 1200px;
    overflow: hidden;
    background: var(--page);
  }
  .canvas {
    position: relative;
    width: 1200px;
    height: 1200px;
  }
  .label {
    position: absolute;
    left: 190px;
    top: 44px;
    width: 821px;
    height: 1111px;
    background: var(--white);
    overflow: hidden;
    font-family: "Oswald", sans-serif;
  }
  .header-band {
    position: absolute;
    left: 0; top: 0;
    width: 821px; height: 419px;
    background: linear-gradient(180deg, var(--red-deep) 0%, var(--red) 70%, var(--red-bright) 100%);
  }
  .brand {
    position: absolute;
    top: 68px; left: 0; width: 100%;
    text-align: center;
    font-weight: 700;
    font-size: 58px;
    line-height: 58px;
    letter-spacing: 2px;
    color: var(--white);
  }
  .title {
    position: absolute;
    top: 190px; left: 0; width: 100%;
    margin: 0;
    text-align: center;
    font-family: "Anton", sans-serif;
    font-weight: 400;
    font-size: 98px;
    line-height: 108px;
    color: var(--white);
    letter-spacing: 0.5px;
  }
  .usage-tab {
    position: absolute;
    left: 183px; top: 418px;
    width: 456px; height: 132px;
  }
  .usage-text {
    position: absolute;
    left: 183px; top: 432px;
    width: 456px;
    text-align: center;
    font-weight: 500;
    font-size: 36px;
    line-height: 52px;
    color: var(--white);
  }
  .benefits {
    position: absolute;
    top: 560px; left: 0;
    margin: 0; padding: 0;
    list-style: none;
  }
  .benefit {
    position: absolute;
    white-space: nowrap;
    font-weight: 600;
    font-size: 34px;
    line-height: 46px;
    color: var(--ink);
    padding-left: 52px;
  }
  .benefit svg {
    position: absolute;
    left: 0; top: -4px;
    width: 48px; height: 44px;
  }
  .benefit--one { left: 243px; top: 0; }
  .benefit--two { left: 195px; top: 46px; }
  .benefit--three { left: 157px; top: 92px; }
  .pest-emblem {
    position: absolute;
    left: 290px; top: 709px;
    width: 194px; height: 194px;
    border-radius: 50%;
    background: radial-gradient(circle at 50% 50%, var(--mouse-brown) 0%, #a0746a 45%, #c62a2e 70%, #9c1016 100%);
  }
  .formula-ribbon {
    position: absolute;
    left: 322px; top: 880px;
    width: 215px; height: 80px;
  }
  .formula-text {
    position: absolute;
    left: 322px; top: 886px;
    width: 215px;
    text-align: center;
    font-weight: 700;
    font-size: 25px;
    line-height: 30px;
    color: var(--white);
  }
  .footer-band {
    position: absolute;
    left: 0; top: 968px;
    width: 821px; height: 143px;
    background: linear-gradient(180deg, var(--red-bright) 0%, var(--red) 100%);
  }
  .ingredients {
    position: absolute;
    left: 322px; top: 986px;
    width: 206px;
    text-align: center;
    font-weight: 600;
    font-size: 18px;
    line-height: 23px;
    white-space: nowrap;
    color: var(--white);
  }
  .seal {
    position: absolute;
    width: 100px; height: 100px;
    border-radius: 50%;
    box-sizing: border-box;
  }
  .seal--natural {
    left: 210px; top: 966px;
    background: var(--seal-dark);
    border: 7px solid var(--green);
  }
  .seal--safety {
    left: 538px; top: 960px;
    background: var(--green-dark);
    border: 7px solid var(--green-light);
  }
</style>
</head>
<body>
<main class="canvas">
  <section class="label">
    <div class="header-band"></div>
    <div class="brand">VERMAWAY</div>
    <h1 class="title">MOUSE &amp; RAT<br>INFESTATION</h1>

    <svg class="usage-tab" viewBox="0 0 456 132" aria-hidden="true">
      <polygon points="0,0 456,0 424,132 32,132" fill="var(--red-bright)"/>
    </svg>
    <div class="usage-text">SAFE FOR INDOR<br>OUTDOOR USE</div>

    <ul class="benefits">
      <li class="benefit benefit--one">
        <svg viewBox="0 0 48 44" aria-hidden="true"><path d="M4 24 L16 36 L44 6" fill="none" stroke="var(--green)" stroke-width="8" stroke-linecap="round" stroke-linejoin="round"/></svg>
        NATURAL BAIT
      </li>
      <li class="benefit benefit--two">
        <svg viewBox="0 0 48 44" aria-hidden="true"><path d="M4 24 L16 36 L44 6" fill="none" stroke="var(--green)" stroke-width="8" stroke-linecap="round" stroke-linejoin="round"/></svg>
        FREE OF PESTICIDES
      </li>
      <li class="benefit benefit--three">
        <svg viewBox="0 0 48 44" aria-hidden="true"><path d="M4 24 L16 36 L44 6" fill="none" stroke="var(--green)" stroke-width="8" stroke-linecap="round" stroke-linejoin="round"/></svg>
        LONG LASTING CONTROL
      </li>
    </ul>

    <div class="pest-emblem" role="img" aria-label="Photo of a mouse inside a red prohibition sign"></div>

    <div class="footer-band"></div>

    <svg class="formula-ribbon" viewBox="0 0 215 80" aria-hidden="true">
      <polygon points="14,0 215,0 201,80 0,80" fill="var(--green)"/>
    </svg>
    <div class="formula-text">ADVANCED<br>FORMULA</div>

    <div class="seal seal--natural"></div>
    <div class="ingredients">ACTIVE INGREDIENTS:<br>48% PEPPERMINT OIL<br>52% SMART INGREDIENTS</div>
    <div class="seal seal--safety"></div>
  </section>
</main>
</body>
</html>
```